Job Coaching - Falo; engaging people to improve their work experience

design a website focussed on people
with 4 tabs/pages (+2)
1) landing page
2) Professional
3) Job Coaching
4) Bio
5) Contact
6) references

I've added the text to be used in the documents. The website will be in Dutch, but I've added the translations in green just for you to understand what it is about.

I've added my logo as well, and a flyer I used already. this gives you an idea on how it could look like
Pictures you can find there as well. Other pictures can be added of course
The techical creation of the website is not needed. I need all the designs and information to be able to create it myself.

```html
<!DOCTYPE html>
<html lang="nl">
<head>
<meta charset="utf-8">
<title>Falo – Bio</title>
<link href="https://fonts.googleapis.com/css2?family=Nunito:wght@800;900&family=Open+Sans:wght@400;700&family=Poppins:wght@400;500;600&display=swap" rel="stylesheet">
<style>
:root{
  --teal:#1e9fbf;
  --teal-light:#a9dcea;
  --ink:#1b2a33;
  --text:#2a2f33;
  --header-bg:#f3f5f7;
  --band-bg:#e4f1f5;
  --violet:#6d4f8f;
  --blue:#3f67ad;
  --white:#ffffff;
}
*{margin:0;padding:0;box-sizing:border-box}
html,body{width:902px;height:1200px;overflow:hidden;background:var(--white)}
body{position:relative;font-family:"Open Sans",sans-serif;color:var(--text)}
.abs{position:absolute}
.topbar{left:0;top:0;width:902px;height:22px;background:var(--teal);color:var(--white);font:500 7.5px/22px "Poppins",sans-serif;text-align:center}
.topbar u{font-weight:600}
.header{left:0;top:22px;width:902px;height:56px;background:var(--header-bg)}
.brand{left:119px;top:17px;display:flex;align-items:center;gap:6px;font:600 22px/1 "Poppins",sans-serif;color:var(--teal)}
.brand i{display:block;width:16px;height:16px;border-radius:50%;background:var(--teal)}
.nav a{position:absolute;top:23px;font:500 9px/1 "Poppins",sans-serif;color:var(--ink);text-decoration:none;white-space:nowrap}
.nav .active::after{content:"";position:absolute;left:-7px;right:-7px;top:14px;height:3px;background:var(--teal-light)}
.search{left:686px;top:24px}
.btn{display:flex;align-items:center;justify-content:center;color:var(--white);font:500 9px/1 "Poppins",sans-serif;border-radius:3px;background:linear-gradient(90deg,var(--violet),var(--blue))}
.btn-contact{left:717px;top:36px;width:69px;height:28px}
h1{left:115px;top:122px;width:400px;font:900 20px/25px "Nunito",sans-serif;color:var(--ink)}
.copy{font-size:10px;line-height:17.5px;text-align:justify}
.copy p+p{margin-top:12.5px}
.copy b{font-weight:700;color:var(--ink)}
.p-intro{left:116px;top:194px;width:410px}
.p-journey{left:118px;top:349px;width:656px;text-align:left}
.p-career{left:314px;top:431px;width:472px}
.p-father{left:116px;top:707px;width:670px}
.backdrop{background:var(--teal-light)}
.bd-question{left:566px;top:138px;width:180px;height:192px;transform:rotate(2.5deg)}
.img-question{left:583px;top:150px;width:202px;height:167px;background:linear-gradient(135deg,#d9dbdd,#8f9396 55%,#c4c6c8)}
.bd-portrait{left:122px;top:440px;width:174px;height:220px;transform:rotate(-2deg)}
.img-portrait{left:129px;top:445px;width:161px;height:215px;background:linear-gradient(160deg,#b9b3a6,#8d4a4a 55%,#3b2b2e)}
.band{left:0;top:808px;width:902px;height:186px;background:var(--band-bg);overflow:hidden}
.band-photo{left:220px;top:0;width:440px;height:186px;background:radial-gradient(ellipse at 50% 85%,#c7d7df 0,#d7e6ec 45%,rgba(228,241,245,0) 75%)}
.band h2{left:0;top:37px;width:902px;text-align:center;font:900 20px/29px "Nunito",sans-serif;color:var(--ink)}
.btn-cta{left:348px;top:119px;width:208px;height:29px}
.footer h3{font:500 11px/1 "Poppins",sans-serif;color:var(--ink)}
.foot{font:400 10px/1 "Poppins",sans-serif;color:var(--ink)}
.foot-row{display:flex;align-items:flex-start;gap:8px;position:absolute;left:116px}
.foot a{color:var(--ink)}
.legal{left:329px;top:1058px}
.legal div{margin-bottom:12.5px}
.social{left:498px;top:1052px;display:flex;gap:5px}
.social span{width:20px;height:20px;border-radius:50%;background:var(--teal);display:block}
.totop{left:745px;top:1025px;display:flex;align-items:center;gap:7px;font:500 9px/1 "Poppins",sans-serif;color:var(--ink)}
</style>
</head>
<body>
<div class="abs topbar"><u>Meld je aan</u> voor een vrijblijvend kennismakingsgesprek &gt;&gt;</div>

<header class="abs header">
  <div class="abs brand"><i></i>Falo</div>
  <nav class="nav">
    <a style="left:319px">Home</a>
    <a style="left:374px">Professional</a>
    <a style="left:445px">Loopbaanbegeleiding</a>
    <a class="active" style="left:569px">Bio</a>
    <a style="left:610px">Referenties</a>
  </nav>
  <svg class="abs search" width="11" height="11" viewBox="0 0 11 11"><circle cx="4.5" cy="4.5" r="3.4" fill="none" stroke="#555" stroke-width="1.6"/><line x1="7" y1="7" x2="10" y2="10" stroke="#555" stroke-width="1.8" stroke-linecap="round"/></svg>
  <div class="abs btn btn-contact">Contact</div>
</header>

<h1 class="abs">Wat is je beroep?&nbsp; – is vaak de eerste vraag die mensen aan elkaar stellen</h1>

<div class="abs copy p-intro">
  <p>De job die je uitoefent - en hoe je je daarbij voelt - bepaalt voor een groot deel iemands zelfbeeld en identiteit. Het is daarom belangrijk dat je een job vindt die bij jou past.</p>
  <p>Ik spreek uit eigen ervaring. Tijdens mijn opleiding Psychologie (Universiteit Noordveld) heb ik bewust voor de afstudeerrichting Arbeidspsychologie gekozen. De wisselwerking tussen professionele en persoonlijke groei en hoe deze te stimuleren, vond – en vind ik nog steeds – ronduit fascinerend.</p>
</div>

<div class="abs backdrop bd-question"></div>
<div class="abs img-question" role="img" aria-label="Foto: veel grijze vraagtekens met één rood vraagteken"></div>

<div class="abs copy p-journey">
  <p>De opleiding vormde het startschot voor mijn eigen zoektocht. Ook letterlijk. Na het behalen van mijn Master in de Arbeidspsychologie ben ik te voet naar Santiago de Compostella getrokken. Enkele jaren later ben ik samen met mijn (toen nog toekomstige) vrouw naar Rome gewandeld. We stapten gemiddeld acht uur per dag. Hoe dat ging? Zoals alles in het leven, <b>stap voor stap</b>.</p>
</div>

<div class="abs backdrop bd-portrait"></div>
<div class="abs img-portrait" role="img" aria-label="Portretfoto van de coach in een rood hemd"></div>

<div class="abs copy p-career">
  <p>Ook professioneel heb ik de afgelopen vijftien jaar binnen Human Resources een lange weg afgelegd. Zo heb ik gewerkt in verschillende sectoren (ICT, High Tech, Telecom en metaalverwerking), zowel in België als in het buitenland (China en Indië). Hierdoor beschik ik over een ruime ervaring als Recruiter, Business Partner, Project Manager en Talent Manager. Ik kreeg de kans om professionals te begeleiden in hun groeiproces en dit gaf mij enorm veel voldoening en energie.</p>
  <p>Op een bepaald moment volgde ik zelf een coachingstracject, en toen ervaarde ik wat een verschil dit kan betekenen: dankzij coaching word je je meer bewust van jezelf en je mogelijkheden. Als je vertrekt vanuit je eigen kracht, geraak je verder. Inspiratie vind je onderweg.</p>
  <p>Om me als coach verder te specialiseren heb ik de opleiding tot Associated Certified Coach (ACF-label) gevolgd bij CoachKompas. Daarna heb ik mij aangemeld voor de cursus Loopbaanbegeleider bij het Coachwerkplaats om zo mijn expertise nog verder uit te bouwen.</p>
</div>

<div class="abs copy p-father">
  <p>Meer nog dan mijn professionele vorming en ervaringen heeft het <b>vaderschap</b> mij gemaakt tot de mens en coach die ik nu ben. Als vader van twee prachtige zonen en een geweldige dochter weet ik dat het niet altijd eenvoudig is om een gezonde work-life balance te bewaren. Het vaderschap heeft mij geleerd mild te zijn - voor anderen én voor mezelf-, open te communiceren en een sterke vertrouwensband te ontwikkelen. Eigenschappen die als coach onontbeerlijk zijn.</p>
</div>

<section class="abs band">
  <div class="abs band-photo" role="img" aria-label="Vervaagde foto van een man die juichend de armen opsteekt"></div>
  <h2 class="abs">Ik heb de job van mijn leven gevonden.<br>Jij binnenkort ook?</h2>
  <div class="abs btn btn-cta">Vraag hier je kennismakingsgesprek aan</div>
</section>

<footer class="footer">
  <h3 class="abs" style="left:116px;top:1021px">Falo Coaching</h3>
  <h3 class="abs" style="left:329px;top:1021px">Juridisch</h3>
  <h3 class="abs" style="left:498px;top:1021px">Volg mij</h3>

  <div class="foot foot-row" style="top:1056px">
    <svg width="13" height="13" viewBox="0 0 24 24"><path fill="#1e9fbf" d="M6.6 10.8a15 15 0 0 0 6.6 6.6l2.2-2.2a1 1 0 0 1 1-.25 11.4 11.4 0 0 0 3.6.57 1 1 0 0 1 1 1V20a1 1 0 0 1-1 1A17 17 0 0 1 3 4a1 1 0 0 1 1-1h3.5a1 1 0 0 1 1 1c0 1.25.2 2.45.57 3.57a1 1 0 0 1-.25 1z"/></svg>
    <span>+32 470 18 44 09</span>
  </div>
  <div class="foot foot-row" style="top:1091px">
    <svg width="16" height="11" viewBox="0 0 16 11"><rect width="16" height="11" fill="#1e9fbf"/><path d="M0 0l8 6 8-6M0 11l6-5M16 11l-6-5" stroke="#fff" stroke-width="1" fill="none"/></svg>
    <a style="text-decoration:underline">Stuur een bericht</a>
  </div>
  <div class="foot foot-row" style="top:1127px;line-height:15px">
    <svg width="12" height="15" viewBox="0 0 12 15" style="margin-top:-1px"><path d="M6 0a6 6 0 0 1 6 6c0 4-6 9-6 9S0 10 0 6a6 6 0 0 1 6-6z" fill="#1e9fbf"/><circle cx="6" cy="6" r="2.2" fill="#fff"/></svg>
    <span>Lindenhofstraat 12<br>2000 ANTWERPEN</span>
  </div>

  <div class="abs foot legal">
    <div>Algemene voorwaarden</div>
    <div>Privacyverklaring</div>
    <div>Sitemap</div>
  </div>

  <div class="abs social" aria-label="Sociale media"><span></span><span></span><span></span></div>

  <div class="abs totop">
    <svg width="10" height="7" viewBox="0 0 10 7"><path d="M1 6l4-4 4 4" fill="none" stroke="#1b2a33" stroke-width="1.6"/></svg>
    Top
  </div>
</footer>
</body>
</html>
```